Creative/innovative law firm website

A law firm website that immediately looks different from other law firm websites. We like the color scheme (dark background with warm, neutral colors) and simple, organic logos (trees, leaves, etc.) of this website: https://brambleworth.legal/

We'll be offering creative/innovative solutions to complex problems faced by state governments, industries, other law firms, and individuals. We're located in Montana (U.S.A.), and the outdoors is a huge part of our lives and identities.

We will need a home page, an "About Us" page with a separate subpage for each attorney (two attorneys), a blog or "Publications" page, a payment portal (which will integrate with Quillo), and a "Services" page.

```html
<!DOCTYPE html>
<html lang="en">
<head>
<meta charset="utf-8">
<title>Larchmont &amp; Sedgewick P.C.</title>
<link href="https://fonts.googleapis.com/css2?family=Montserrat:wght@400;500;600;700&family=Tinos:wght@400;700&display=swap" rel="stylesheet">
<style>
:root{
  --orange:#d9861e;
  --orange-dark:#c2741a;
  --black:#000;
  --ink:#1b1b1b;
  --muted:#6f6f6f;
  --cream:#faf0e2;
  --white:#fff;
  --line:#d8d8d8;
}
*{box-sizing:border-box;margin:0;padding:0}
html,body{width:1200px;height:4298px;overflow:hidden}
body{position:relative;background:var(--white);font-family:"Montserrat",sans-serif;color:var(--ink)}
.abs{position:absolute}
.serif{font-family:"Tinos",serif}
.btn{position:absolute;background:var(--orange);color:#fff;font-family:"Tinos",serif;font-weight:700;font-size:15px;letter-spacing:.5px;display:flex;align-items:center;justify-content:center;border-radius:0 0 14px 0}
.kicker{color:var(--orange);font-size:12px;letter-spacing:.5px}
.h2{font-family:"Tinos",serif;font-weight:700;font-size:30px;letter-spacing:.5px}
.rule{position:absolute;height:2px;width:36px;background:var(--orange)}
.centered{left:0;width:1200px;text-align:center}
.para{font-size:11.5px;line-height:19px;color:var(--muted)}

/* header */
.topbar{left:0;top:0;width:1200px;height:100px;background:var(--black)}
.brand{left:60px;top:14px;display:flex;align-items:center;gap:12px;color:#fff}
.brand-mark{width:40px;height:40px;border-radius:50%;background:var(--orange)}
.brand-name{font-family:"Tinos",serif;font-weight:700;font-size:20px;line-height:22px}
.consult{top:16px;color:#fff}
.consult small{display:block;color:var(--orange);font-size:10px;letter-spacing:.4px}
.consult b{font-family:"Tinos",serif;font-size:23px}
.navbar{left:60px;top:75px;width:1080px;height:46px;background:var(--orange);border-radius:0 0 14px 14px;z-index:3;display:flex;align-items:center}
.navbar a{color:#fff;font-size:10.5px;text-decoration:none;margin-left:31px;margin-right:20px;letter-spacing:.3px}
.social-top{position:absolute;right:0;top:0;height:46px;display:flex;align-items:center;border-left:1px solid rgba(0,0,0,.2);padding:0 14px;gap:14px}
.social-top span{font-size:13px;font-weight:700;color:var(--black)}

/* hero */
.hero{left:0;top:100px;width:1200px;height:613px;background:linear-gradient(100deg,#2b2620 0%,#4b4035 40%,#6f5b47 65%,#2f2924 100%)}
.hero-title{left:58px;top:305px;color:#fff;font-weight:700;font-size:58px;line-height:60px;letter-spacing:-1px}
.hero-title em{font-style:normal;color:var(--orange)}
.hero-sub{left:63px;top:440px;color:#fff;font-size:16px}
.arrow{top:400px;width:34px;height:40px;background:rgba(217,134,30,.4);display:flex;align-items:center;justify-content:center}

/* about */
.about-bar{left:217px;top:713px;width:125px;height:637px;background:var(--orange)}

/* services */
.services{left:0;top:1350px;width:1200px;height:503px;background:var(--black)}
.svc{position:absolute;top:202px;width:300px;height:301px}
.svc-label{position:absolute;left:0;bottom:22px;width:100%;text-align:center;color:#fff;font-family:"Tinos",serif;font-weight:700;font-size:15px;letter-spacing:.3px}
.svc-band{position:absolute;left:0;bottom:0;width:100%;height:75px;background:var(--orange)}

/* experts */
.experts{left:0;top:1853px;width:1200px;height:450px;background:var(--cream)}
.tile{position:absolute;width:224px;height:66px;background:#fff;display:flex;align-items:center;justify-content:center;gap:8px;font-size:20px;font-weight:600}
.tile i{display:block;width:16px;height:16px}

/* solutions */
.box{position:absolute;top:2549px;width:174px;height:183px;border:1.5px solid #9a9a9a;text-align:center}
.box svg{margin-top:24px}
.box p{font-family:"Tinos",serif;font-weight:700;font-size:15px;line-height:19px;margin-top:8px}
.box .rule{left:72px;top:147px;width:30px}
.box.active{background:var(--orange);border-color:var(--orange)}
.box.active .rule{background:#fff}

/* blog */
.blog-band{left:0;top:3150px;width:786px;height:335px;background:var(--orange)}
.post-img{top:3001px;width:282px;height:247px}
.post-title{font-family:"Tinos",serif;font-weight:700;font-size:17px;line-height:24px;color:var(--ink)}
.post-text{font-size:11px;line-height:19px;color:#fff}
.side-date{color:var(--orange);font-family:"Tinos",serif;font-size:13px}
.side-more{color:var(--orange);font-family:"Tinos",serif;font-weight:700;font-size:13px;text-decoration:underline}

/* contact */
.contact{left:0;top:3485px;width:1200px;height:421px;background:linear-gradient(90deg,#2d2823,#4e4236 45%,#3a322b 70%,#241f1b)}
.contact::after{content:"";position:absolute;inset:0;background:rgba(0,0,0,.35)}
.field{position:absolute;background:#fff;border-radius:4px;font-size:10.5px;color:#555;padding:11px 14px;z-index:2}
.field.first{background:rgba(255,255,255,0);border:1px solid var(--orange);color:var(--orange)}

/* footer */
.footer{left:0;top:3906px;width:1200px;height:392px;background:var(--black);color:#fff}
.ft{font-family:"Tinos",serif;font-weight:700;color:var(--orange);font-size:15px;letter-spacing:.3px}
.ft-list{list-style:none;font-size:11px;line-height:22.5px}
.ft-list li::before{content:"";display:inline-block;width:5px;height:5px;background:var(--orange);transform:rotate(45deg);margin-right:12px;vertical-align:middle}
.circle{width:34px;height:34px;border-radius:50%;background:var(--orange);color:#000;font-weight:700;font-size:13px;display:flex;align-items:center;justify-content:center}
</style>
</head>
<body>

<!-- header -->
<div class="abs topbar"></div>
<div class="abs brand">
  <div class="brand-mark"></div>
  <div class="brand-name">LARCHMONT &amp;<br>SEDGEWICK P.C.</div>
</div>
<svg class="abs" style="left:886px;top:23px" width="22" height="22" viewBox="0 0 22 22"><circle cx="9" cy="9" r="7" fill="none" stroke="#d9861e" stroke-width="2"/><line x1="14" y1="14" x2="20" y2="20" stroke="#d9861e" stroke-width="2"/></svg>
<svg class="abs" style="left:944px;top:20px" width="36" height="34" viewBox="0 0 36 34"><path d="M6 4 L12 4 L14 11 L10 14 Q14 22 21 25 L24 21 L31 23 L31 29 Q29 32 25 32 Q8 28 3 9 Q3 5 6 4Z" fill="none" stroke="#d9861e" stroke-width="2"/><path d="M20 4 Q30 5 32 15 M20 9 Q26 10 27 15" fill="none" stroke="#d9861e" stroke-width="2"/></svg>
<div class="abs consult" style="left:992px"><small>FREE CONSULTATION</small><b>+1 123 456 7890</b></div>

<nav class="abs navbar">
  <a>HOME</a><a>ABOUT US &nbsp;⌵</a><a>SERVICES &nbsp;⌵</a><a>PUBLICATION &nbsp;⌵</a><a>PAYMENTS</a><a>CONTACT US</a>
  <div class="social-top"><span>T</span><span>R</span><span>M</span></div>
</nav>

<!-- hero -->
<div class="abs hero" role="img" aria-label="Photo of two attorneys reviewing a tablet in an office"></div>
<div class="abs hero-title">Larchmont <em>&amp;</em><br>Sedgewick P.C.</div>
<div class="abs hero-sub">Innovative Solutions To Complex Problems</div>
<div class="btn" style="left:60px;top:480px;width:247px;height:42px">REQUEST A CONSULTING</div>
<div class="abs arrow" style="left:0"><svg width="10" height="16"><path d="M8 1 L2 8 L8 15" stroke="#fff" stroke-width="2" fill="none"/></svg></div>
<div class="abs arrow" style="right:0"><svg width="10" height="16"><path d="M2 1 L8 8 L2 15" stroke="#fff" stroke-width="2" fill="none"/></svg></div>

<!-- about -->
<div class="abs about-bar"></div>
<svg class="abs" style="left:142px;top:788px" width="586" height="360" viewBox="0 0 586 360" role="img" aria-label="Photo of an attorney speaking at a courtroom lectern">
  <defs><linearGradient id="court" x1="0" y1="0" x2="1" y2="1"><stop offset="0" stop-color="#5a3d26"/><stop offset=".55" stop-color="#2e2018"/><stop offset="1" stop-color="#120c08"/></linearGradient></defs>
  <path d="M0 360 L0 150 Q20 15 170 0 L586 0 L586 127 L400 127 L400 360 Z" fill="url(#court)"/>
</svg>
<div class="abs kicker" style="left:596px;top:968px">ABOUT US</div>
<div class="abs h2" style="left:596px;top:993px;font-size:27px">LARCHMONT &amp; SEDGEWICK P.C</div>
<div class="abs para" style="left:596px;top:1060px;width:430px">Lorem Ipsum has been the industry's standard dummy text ever since the 1500s, when an unknown printer took a galley of type and scrambled it to make a type specimen book.</div>
<div class="abs para" style="left:596px;top:1125px;width:430px">Lorem Ipsum has been the industry's standard dummy text ever since the when an unknown printer took a galley of type and scrambled it to make a type specimen book. It has survived not only five centuries, but also the leap into electronic typesetting, remaining essentially unchanged.</div>
<div class="btn" style="left:596px;top:1220px;width:155px;height:40px">LEARN MORE</div>

<!-- services -->
<div class="abs services">
  <div class="abs kicker centered" style="top:70px">What We Do</div>
  <div class="abs h2 centered" style="top:95px;color:#fff;font-size:33px">SERVICES WE PROVIDE</div>
  <div class="abs" style="left:532px;top:144px;width:136px;height:1px;background:#555"></div>
  <div class="rule" style="left:582px;top:143px"></div>
  <div class="svc" style="left:0;background:linear-gradient(180deg,#8a8a8a,#3c3c3c)" role="img" aria-label="Photo of a columned government building"><div class="svc-label">STATE GOVERNMENTS</div></div>
  <div class="svc" style="left:300px;background:linear-gradient(180deg,#6b5a3a,#2f2a22)" role="img" aria-label="Photo of a hard hat and gavel"><div class="svc-band"></div>
    <svg style="position:absolute;left:110px;top:85px" width="70" height="60" viewBox="0 0 70 60"><path d="M4 56 L4 26 L18 18 L18 26 L32 18 L32 26 L46 18 L46 4 L58 4 L58 56 Z" fill="none" stroke="#fff" stroke-width="2.5"/><rect x="12" y="36" width="8" height="8" fill="none" stroke="#fff" stroke-width="2"/><rect x="26" y="36" width="8" height="8" fill="none" stroke="#fff" stroke-width="2"/><rect x="40" y="36" width="8" height="8" fill="none" stroke="#fff" stroke-width="2"/><line x1="50" y1="4" x2="50" y2="30" stroke="#fff" stroke-width="2"/><line x1="54" y1="4" x2="54" y2="30" stroke="#fff" stroke-width="2"/></svg>
    <div class="svc-label" style="font-size:19px;bottom:25px">INDUSTRIES</div></div>
  <div class="svc" style="left:600px;background:linear-gradient(180deg,#7a4b45,#3b3b48 60%,#2a3b55)" role="img" aria-label="Photo of a handshake before national flags"><div class="svc-label">INDIVIDUALS</div></div>
  <div class="svc" style="left:900px;background:linear-gradient(180deg,#8a8174,#4a4540)" role="img" aria-label="Photo of scales of justice on a lawyer's desk"><div class="svc-label">OTHER LAW FIRMS</div></div>
</div>

<!-- experts -->
<div class="abs experts">
  <div class="abs kicker" style="left:130px;top:157px">WHO WORK WITH</div>
  <div class="abs h2" style="left:130px;top:182px;font-size:28px">EXPERTS WE WORK WITH</div>
  <div class="rule" style="left:130px;top:224px"></div>
  <div class="btn" style="left:130px;top:255px;width:180px;height:40px">MEET ATTORNEY</div>
  <div class="tile" style="left:618px;top:85px;color:#1a1f3c;font-size:17px;font-weight:700"><i style="background:#1a1f3c"></i>VERANOTE</div>
  <div class="tile" style="left:850px;top:85px;color:#3a9fc5;background:#fdf7ef;font-size:19px">Tallgrass Suite</div>
  <div class="tile" style="left:618px;top:159px;color:#6b6b6b;font-size:16px;background:#fdf7ef"><i style="background:#6aa33f;border-radius:50%"></i>Sunmere</div>
  <div class="tile" style="left:850px;top:159px;color:#e04b1a"><i style="background:#e04b1a"></i>Deskwork</div>
  <div class="tile" style="left:618px;top:233px;color:#2a73b8"><i style="background:#2a73b8;border-radius:50%"></i>Brieflo</div>
  <div class="tile" style="left:850px;top:233px;color:#1a1a1a;background:#fdf7ef;font-weight:700"><i style="background:#4c9a3a"></i>Docsway</div>
  <div class="tile" style="left:618px;top:307px;color:#3a8fd0;background:#fdf7ef;font-weight:700">Docketry</div>
  <div class="tile" style="left:850px;top:307px;color:#9a9a9a;font-weight:400;font-size:24px"><i style="background:#b6c9d6;border-radius:50%;width:22px;height:22px"></i>Lexmora</div>
</div>

<!-- solutions -->
<div class="abs kicker centered" style="top:2377px">WHAT WE DO</div>
<div class="abs h2 centered" style="top:2402px;font-size:28px">SOLUTIONS WE OFFERS</div>
<div class="abs" style="left:545px;top:2447px;width:110px;height:1px;background:#ddd"></div>
<div class="rule" style="left:582px;top:2446px"></div>
<div class="abs para centered" style="top:2473px;font-size:11px"><div style="width:520px;margin:0 auto">Lorem Ipsum has been the industry's standard dummy text ever since the when an unknown printer took a galley of type and scrambled make.</div></div>

<div class="box" style="left:220px">
  <svg width="40" height="52" viewBox="0 0 40 52"><circle cx="20" cy="13" r="9" fill="none" stroke="#d9861e" stroke-width="2"/><path d="M4 50 L4 38 Q4 27 20 27 Q36 27 36 38 L36 50 Z M20 27 L20 50 M14 28 L20 36 L26 28" fill="none" stroke="#d9861e" stroke-width="2"/></svg>
  <p>Professional<br>Lawyers</p><div class="rule"></div></div>
<div class="box active" style="left:416px">
  <svg width="52" height="52" viewBox="0 0 52 52"><path d="M8 4 L32 4 L40 12 L40 48 L8 48 Z" fill="none" stroke="#fff" stroke-width="2"/><line x1="14" y1="16" x2="30" y2="16" stroke="#fff" stroke-width="2"/><line x1="14" y1="23" x2="26" y2="23" stroke="#fff" stroke-width="2"/><circle cx="32" cy="33" r="9" fill="none" stroke="#fff" stroke-width="2"/><path d="M28 33 L31 36 L36 30" fill="none" stroke="#fff" stroke-width="2"/><line x1="39" y1="40" x2="48" y2="49" stroke="#fff" stroke-width="3"/></svg>
  <p style="color:#1b1b1b">Document<br>Reviewing</p><div class="rule"></div></div>
<div class="box" style="left:611px">
  <svg width="54" height="52" viewBox="0 0 54 52"><path d="M6 10 L13 8 L17 17 L13 21 Q17 30 25 34 L29 30 L38 34 L36 42 Q30 46 22 42 Q6 32 4 16 Z" fill="none" stroke="#d9861e" stroke-width="2"/><circle cx="38" cy="15" r="12" fill="none" stroke="#d9861e" stroke-width="2"/><text x="38" y="19" font-size="11" font-family="Montserrat,sans-serif" fill="#d9861e" text-anchor="middle">24</text></svg>
  <p>24 /<br>Support</p><div class="rule"></div></div>
<div class="box" style="left:806px">
  <svg width="70" height="52" viewBox="0 0 70 52"><path d="M35 4 L39 14 L50 15 L42 22 L44 33 L35 27 L26 33 L28 22 L20 15 L31 14 Z" fill="none" stroke="#d9861e" stroke-width="2"/><path d="M14 24 L17 31 L24 32 L19 37 L20 44 L14 40 L8 44 L9 37 L4 32 L11 31 Z" fill="none" stroke="#d9861e" stroke-width="2"/><path d="M56 24 L59 31 L66 32 L61 37 L62 44 L56 40 L50 44 L51 37 L46 32 L53 31 Z" fill="none" stroke="#d9861e" stroke-width="2"/></svg>
  <p>Discounted<br>Rate</p><div class="rule"></div></div>

<!-- blog -->
<div class="abs h2" style="left:100px;top:2850px;font-size:29px">BLOG POST</div>
<div class="rule" style="left:102px;top:2898px;width:34px"></div>
<div class="abs para" style="left:102px;top:2918px;width:420px;font-size:11px">Lorem Ipsum has been the industry's standard dummy text ever since the when an unknown printer took a galley.</div>
<div class="abs blog-band"></div>
<div class="abs post-img" style="left:102px;background:linear-gradient(160deg,#5f7486,#233240)" role="img" aria-label="Photo of two businessmen talking in a glass office"></div>
<div class="abs post-img" style="left:437px;background:linear-gradient(160deg,#6f665c,#2a2623)" role="img" aria-label="Photo of a team reviewing documents at a table"></div>
<div class="abs post-title" style="left:102px;top:3275px;width:300px">Lorem Ipsum has been the industry<br>Standard dummy text ever.</div>
<div class="abs post-text" style="left:100px;top:3335px;width:290px">Lorem Ipsum has been the industry's standard dummy text ever since the when an unknown printer took a galley has been the</div>
<div class="abs post-title" style="left:438px;top:3275px;width:300px">Lorem Ipsum has been the industry<br>Standard dummy text ever.</div>
<div class="abs post-text" style="left:436px;top:3335px;width:290px">Lorem Ipsum has been the industry's standard dummy text ever since the when an unknown printer took a galley has been the</div>

<div class="abs side-date" style="left:865px;top:3015px">7 Dec 2021</div>
<div class="abs post-title" style="left:865px;top:3040px">Lorem Ipsum has industr<br>Standard text Ever.</div>
<div class="abs para" style="left:863px;top:3096px;width:260px;font-size:11px">Lorem Ipsum has been the industry's stand dummy text ever since the when unknown printer took a galley has been the</div>
<div class="abs side-more" style="left:865px;top:3170px">Read More</div>
<div class="abs" style="left:851px;top:3231px;width:289px;height:1px;background:var(--line)"></div>
<div class="abs side-date" style="left:865px;top:3277px">7 Dec 2021</div>
<div class="abs post-title" style="left:865px;top:3302px">Lorem Ipsum has industr<br>Standard text Ever.</div>
<div class="abs para" style="left:863px;top:3358px;width:260px;font-size:11px">Lorem Ipsum has been the industry's stand dummy text ever since the when unknown printer took a galley has been the</div>
<div class="abs side-more" style="left:865px;top:3432px">Read More</div>

<!-- contact -->
<div class="abs contact" role="img" aria-label="Photo of an attorney standing by an office window"></div>
<div class="abs kicker centered" style="top:3561px;z-index:2">Stay In Touch</div>
<div class="abs h2 centered" style="top:3585px;color:#fff;font-size:28px;z-index:2">CONTACT US</div>
<div class="abs centered" style="top:3648px;z-index:2;font-size:11.5px;line-height:20px;color:#ddd"><div style="width:460px;margin:0 auto">Lorem Ipsum has been the industry's standard dummy text ever since the when an unknown printer took a galley.</div></div>
<div class="field first" style="left:170px;top:3730px;width:236px;height:39px">Name *</div>
<div class="field" style="left:417px;top:3730px;width:236px;height:39px">Email *</div>
<div class="field" style="left:664px;top:3730px;width:236px;height:92px">Message *</div>
<div class="field" style="left:170px;top:3784px;width:236px;height:38px">Phone *</div>
<div class="field" style="left:417px;top:3784px;width:236px;height:38px">Services *<span style="position:absolute;right:14px;color:#d9861e">▾</span></div>
<div class="btn" style="left:918px;top:3757px;width:110px;height:40px;z-index:2;border-radius:0 0 14px 0">SUBMIT</div>

<!-- footer -->
<div class="abs footer">
  <div class="abs" style="left:62px;top:44px;display:flex;gap:12px;align-items:center">
    <div class="brand-mark" style="width:52px;height:52px"></div>
    <div class="serif" style="font-size:23px;line-height:27px;font-weight:700">Larchmont &amp;<br>Sedgewick P.C.</div>
  </div>
  <div class="abs" style="left:62px;top:136px;width:345px;font-size:11px;line-height:21px;color:#ddd">Lorem Ipsum has been the industry's standard dummy text ever since the when an unknown printer took a galley of type and scrambled make.</div>

  <div class="abs ft" style="left:464px;top:45px">SITEMAP</div>
  <ul class="abs ft-list" style="left:464px;top:78px"><li>Home</li><li>About Us</li><li>Services</li><li>Publication</li><li>Payments</li></ul>

  <div class="abs ft" style="left:694px;top:45px">CONTACT US</div>
  <svg class="abs" style="left:694px;top:80px" width="16" height="22" viewBox="0 0 16 22"><path d="M8 21 Q1 12 1 8 A7 7 0 0 1 15 8 Q15 12 8 21Z" fill="none" stroke="#d9861e" stroke-width="2"/><circle cx="8" cy="8" r="2.5" fill="#d9861e"/></svg>
  <div class="abs" style="left:728px;top:80px;font-size:11px;line-height:19px"><span style="color:#d9861e">Larchmont &amp; Sedgewick P.C.</span><br>101 - lorem ipsum simple text<br>print type setting industry.</div>
  <svg class="abs" style="left:694px;top:146px" width="18" height="18" viewBox="0 0 18 18"><path d="M3 1 L7 1 L8 5 L6 7 Q8 11 11 12 L13 10 L17 11 L17 15 Q16 17 13 17 Q3 14 1 4 Q1 2 3 1Z" fill="#d9861e"/></svg>
  <div class="abs" style="left:728px;top:147px;font-size:14px">123 456 7890</div>
  <svg class="abs" style="left:694px;top:181px" width="18" height="13" viewBox="0 0 18 13"><rect width="18" height="13" rx="1" fill="#d9861e"/><path d="M1 1 L9 7 L17 1" stroke="#000" stroke-width="1.5" fill="none"/></svg>
  <div class="abs" style="left:728px;top:179px;font-size:11.5px">info@larchmont.com</div>

  <div class="abs ft" style="left:923px;top:45px">LACATION MAP</div>
  <div class="abs" style="left:921px;top:80px;width:219px;height:128px;background:linear-gradient(135deg,#bcd7ee,#9ec6e6)" role="img" aria-label="Map showing the office location"></div>

  <div class="abs" style="left:62px;top:255px;width:1078px;height:1px;background:#333"></div>
  <div class="abs" style="left:538px;top:289px;display:flex;gap:8px"><div class="circle">T</div><div class="circle">R</div><div class="circle">M</div></div>
  <div class="abs centered" style="top:341px;font-size:10.5px;color:#ccc"><span style="color:#d9861e">©Larchmont &amp; Sedgewick P.C.</span> - 2021 All rights reserved.</div>
</div>

</body>
</html>
```